Truck Drivers Using App w/Jobsite Checklist

Looking for an 8" x 11" flyer that conveys to our customers (roofing contractors) that our drivers have tablets in each truck that have an app with a jobsite checklist that gives contractors less real time notifications and mistakes are caught with photos.
Should read something like this:
Ever wonder if your material has been delivered? We've got a solution for that!
All Trucks are equipped with dash-mounted tablet.
Here's what you get access to:
- Real Time Email Confirmation of Delivery
- Photos of Material Placement
- Before/After Photo of Driveway
- Material List of Products Delivered
- Homeowner Sign Off
Maybe a collage of the different photos available.
Target Market(s)
Roofing/Building Contractors
Industry/Entity Type
Roofing
Requirements
Must have
- website: www.harborfinchdepot.com
- tagline: Building Relationships, Building Trust - a Tradition Since 1905
- Photoshop format for further editing
Nice to have
- A smooth look to it.
- A collage of the photos avail on app

```html
<!DOCTYPE html>
<html lang="en">
<head>
<meta charset="utf-8">
<title>Harbor Finch Depot – Delivery Tablet Flyer</title>
<link href="https://fonts.googleapis.com/css2?family=Lato:wght@400;700;900&display=swap" rel="stylesheet">
<style>
  :root{
    --blue:#1463ac;
    --blue-dark:#0e4f8c;
    --charcoal:#3a3a3c;
    --ink:#222;
    --paper:#f4f4f4;
    --white:#fff;
    --backdrop:#e4e5e9;
    --rule:#cfcfcf;
  }
  *{box-sizing:border-box;margin:0;padding:0}
  html,body{width:1200px;height:800px;overflow:hidden;background:var(--backdrop);font-family:"Lato",sans-serif}
  .flyer{position:absolute;left:310px;top:25px;width:580px;height:750px;background:var(--paper);overflow:hidden;box-shadow:0 6px 18px rgba(0,0,0,.15)}
  .abs{position:absolute}
  .frame-lines{left:0;top:0}
  .brand{left:22px;top:44px;display:flex;align-items:center;gap:8px}
  .brand-dot{width:22px;height:22px;border-radius:50%;background:var(--blue)}
  .brand-name{font-weight:900;font-size:15px;color:var(--blue);letter-spacing:.5px;text-transform:uppercase;line-height:1.05}
  .headline{right:22px;top:26px;text-align:left;text-transform:uppercase;line-height:.95}
  .headline .lead{display:block;color:var(--blue);font-weight:900;font-size:27px}
  .headline .punch{display:block;color:var(--ink);font-weight:900;font-size:30px}
  .photo{background:linear-gradient(160deg,#9fc1df 0%,#d6d9dc 45%,#6c6e70 100%)}
  .photo-truck{left:18px;top:112px;width:245px;height:268px;clip-path:polygon(0 0,100% 0,100% 100%,0 100%)}
  .photo-dash{left:262px;top:140px;width:318px;height:218px;background:linear-gradient(180deg,#c9ced3 0%,#a9adb0 40%,#2c2d2f 62%,#151516 100%);clip-path:polygon(12% 0,100% 0,100% 100%,0 100%)}
  .solution{left:18px;top:332px;width:255px;height:50px;background:var(--charcoal);color:var(--white);font-weight:900;font-size:14px;text-transform:uppercase;padding:8px 14px;line-height:1.15;clip-path:polygon(0 0,100% 0,94% 100%,0 100%)}
  .band{left:0;top:372px;width:580px;height:112px;background:var(--blue)}
  .band-title{left:0;top:384px;width:580px;text-align:center;color:var(--white);text-transform:uppercase;line-height:1.05}
  .band-title .thin{display:block;font-weight:400;font-size:27px}
  .band-title .bold{display:block;font-weight:900;font-size:31px}
  .ribbon{left:90px;top:450px;width:400px;height:34px;background:var(--charcoal);color:var(--white);text-transform:uppercase;font-size:15px;letter-spacing:.5px;text-align:center;line-height:34px;clip-path:polygon(0 0,100% 0,95% 100%,5% 100%)}
  .features{left:14px;top:500px;width:552px;display:flex}
  .feature{flex:1;display:flex;flex-direction:column;align-items:center;text-align:center;padding:6px 6px;border-right:1px solid var(--rule);min-height:108px}
  .feature:last-child{border-right:none}
  .feature svg{width:34px;height:34px;margin-bottom:8px}
  .feature-label{font-size:12.5px;color:var(--ink);line-height:1.15}
  .collage{top:622px;height:60px}
  .collage-a{left:250px;width:120px;clip-path:polygon(12% 0,100% 0,88% 100%,0 100%);background:linear-gradient(180deg,#e9e7e0,#b9c2c9)}
  .collage-b{left:360px;width:120px;clip-path:polygon(12% 0,100% 0,88% 100%,0 100%);background:linear-gradient(180deg,#5d7fa6,#8c3a3a)}
  .collage-c{left:470px;width:110px;clip-path:polygon(12% 0,100% 0,100% 100%,0 100%);background:linear-gradient(180deg,#c8d2db,#7994b2)}
  .rule-dark{left:0;top:690px;width:330px;height:10px;background:var(--charcoal);clip-path:polygon(0 0,100% 0,97% 100%,0 100%)}
  .footer{left:0;top:706px;width:580px;height:44px;background:var(--blue);color:var(--white);text-align:center;font-size:17px;letter-spacing:3px;line-height:44px}
</style>
</head>
<body>
  <main class="flyer">
    <svg class="abs frame-lines" width="580" height="120" viewBox="0 0 580 120" aria-hidden="true">
      <polygon points="230,0 580,0 580,8 238,8" fill="var(--blue)"/>
      <polygon points="0,30 230,30 238,8 250,8 242,36 0,36" fill="var(--blue)"/>
      <polygon points="250,8 580,8 580,14 256,14" fill="var(--charcoal)"/>
    </svg>

    <div class="abs brand">
      <span class="brand-dot"></span>
      <span class="brand-name">Harbor Finch<br>Depot</span>
    </div>

    <h1 class="abs headline">
      <span class="lead">Ever wonder<br>if your<br>material has</span>
      <span class="punch">been delivered?</span>
    </h1>

    <div class="abs photo photo-truck" role="img" aria-label="Photo of a white flatbed delivery truck with a loader crane carrying roofing material"></div>
    <div class="abs photo-dash" role="img" aria-label="Photo from a truck cab showing the steering wheel, dashboard and a mounted tablet, with the highway ahead"></div>
    <div class="abs solution">We've got a<br>solution for that!</div>

    <div class="abs band"></div>
    <h2 class="abs band-title">
      <span class="thin">All trucks are equipped with</span>
      <span class="bold">Dash-mounted tablet.</span>
    </h2>
    <div class="abs ribbon">Here's what you get access to:</div>

    <ul class="abs features">
      <li class="feature">
        <svg viewBox="0 0 34 34" aria-hidden="true"><rect x="2" y="8" width="26" height="18" rx="2" fill="var(--blue)"/><path d="M2 9 L15 19 L28 9" fill="none" stroke="#fff" stroke-width="2"/><circle cx="27" cy="25" r="6" fill="#fff" stroke="var(--blue)" stroke-width="2"/><path d="M24 25 l2 2 l4 -4" fill="none" stroke="var(--blue)" stroke-width="2"/></svg>
        <span class="feature-label">Real Time Email Confirmation of Delivery</span>
      </li>
      <li class="feature">
        <svg viewBox="0 0 34 34" aria-hidden="true"><rect x="3" y="6" width="24" height="20" fill="none" stroke="var(--blue)" stroke-width="3"/><path d="M6 24 L13 15 L18 20 L21 17 L25 24Z" fill="var(--blue)"/><circle cx="20" cy="11" r="2" fill="var(--blue)"/><path d="M28 22 v8 M24 26 h8" stroke="var(--blue)" stroke-width="2.5"/></svg>
        <span class="feature-label">Photos of Material Placement</span>
      </li>
      <li class="feature">
        <svg viewBox="0 0 34 34" aria-hidden="true"><path d="M5 12 H26 M21 6 L27 12 L21 18" fill="none" stroke="var(--blue)" stroke-width="3.5"/><path d="M29 23 H8 M13 17 L7 23 L13 29" fill="none" stroke="var(--blue)" stroke-width="3.5"/></svg>
        <span class="feature-label">Before/After Photo of Driveway</span>
      </li>
      <li class="feature">
        <svg viewBox="0 0 34 34" aria-hidden="true"><rect x="6" y="5" width="22" height="26" rx="2" fill="var(--blue)"/><rect x="12" y="2" width="10" height="6" rx="1" fill="var(--blue-dark)"/><path d="M10 14 h14 M10 19 h14 M10 24 h10" stroke="#fff" stroke-width="2"/></svg>
        <span class="feature-label">Material List of Products Delivered</span>
      </li>
      <li class="feature">
        <svg viewBox="0 0 34 34" aria-hidden="true"><path d="M10 9 A11 11 0 1 0 24 9" fill="none" stroke="var(--blue)" stroke-width="3.5"/><path d="M17 3 V16" stroke="var(--blue)" stroke-width="3.5"/></svg>
        <span class="feature-label">Homeowner Sign Off</span>
      </li>
    </ul>

    <div class="abs collage collage-a" role="img" aria-label="Photo of a delivery driver in a safety vest using a tablet"></div>
    <div class="abs collage collage-b" role="img" aria-label="Photo of roofing material lifted onto a roof by crane"></div>
    <div class="abs collage collage-c" role="img" aria-label="Photo of wrapped roofing bundles placed on a roof"></div>

    <div class="abs rule-dark"></div>
    <footer class="abs footer">www.harborfinchdepot.com</footer>
  </main>
</body>
</html>
```